KESTRA Communications Business Card- Olde

Kestra Integrated Communications is Corporate communications agency with more than 20 years of experience. We become part of the manegement team of our clients in other to improve their outcomes and grow the possitioning of their brand.
We are in Puerto Rico, latin caribbean island
Name: Marisolde (Olde) Fuentes
787-555-0148
ofuentes@kestrakom.example

Target Market(s)

finance and pharmaceutical companies

Industry/Entity Type

Business

Contact Information for Business Card

modern, edgy colorful and playfull like our logo

Requirements
Must have
• company logo
• name
• tel
• email

```html
<!DOCTYPE html>
<html lang="en">
<head>
<meta charset="utf-8">
<title>Kestra Integrated Communications – Business Card</title>
<link rel="stylesheet" href="https://fonts.googleapis.com/css2?family=Open+Sans:wght@400;600;700&display=swap">
<style>
  :root {
    --bg: #d9d6d2;
    --card-white: #ffffff;
    --brown: #3b2c1a;
    --brown-faint: #4a3720;
    --orange: #f15a24;
    --cream: #ffffff;
    --ink: #3b2c1a;
  }
  * { margin: 0; padding: 0; box-sizing: border-box; }
  html, body { width: 1200px; height: 900px; overflow: hidden; }
  body {
    background: var(--bg);
    font-family: "Open Sans", Arial, sans-serif;
    position: relative;
  }
  .card {
    position: absolute;
    width: 620px;
    height: 354px;
    box-shadow: 0 12px 30px rgba(0,0,0,0.25);
    overflow: hidden;
  }
  /* Front */
  .card-front {
    left: 90px; top: 70px;
    background: var(--card-white);
    display: flex; align-items: center; justify-content: center;
  }
  .front-wordmark {
    display: flex; align-items: center; gap: 22px;
    color: var(--orange);
    font-weight: 700;
    font-size: 92px;
    letter-spacing: 4px;
  }
  .front-wordmark .dot {
    width: 34px; height: 34px; border-radius: 50%;
    background: var(--ink);
  }
  /* Back */
  .card-back {
    left: 490px; top: 476px;
    background: var(--brown);
    color: var(--cream);
  }
  .back-watermark {
    position: absolute; left: 250px; top: 40px;
    font-size: 120px; font-weight: 700;
    color: var(--brown-faint);
    letter-spacing: 6px;
    line-height: 1;
  }
  .back-logo {
    position: absolute; left: 40px; top: 60px;
  }
  .back-logo .name {
    font-size: 54px; font-weight: 700; color: var(--orange);
    letter-spacing: 2px; line-height: 1;
  }
  .back-logo .tagline {
    margin-top: 8px;
    font-size: 11px; font-weight: 600; letter-spacing: 2px;
    color: var(--cream); text-transform: uppercase; line-height: 1.3;
  }
  .band-white {
    position: absolute; right: 0; top: 140px;
    width: 200px; height: 38px;
    background: var(--cream);
  }
  .band-orange {
    position: absolute; left: 0; top: 178px;
    width: 100%; height: 34px;
    background: var(--orange);
  }
  .band-logo {
    position: absolute; right: 70px; top: 150px;
    font-size: 26px; font-weight: 700; color: var(--brown);
    letter-spacing: 1px; line-height: 1;
  }
  .person {
    position: absolute; left: 40px; top: 232px;
    font-size: 21px; font-weight: 700; letter-spacing: 1px;
    text-transform: uppercase; color: var(--cream);
  }
  .contact {
    position: absolute; left: 40px; top: 270px;
    list-style: none;
    font-size: 15px; color: var(--orange);
  }
  .contact li { display: flex; align-items: center; gap: 10px; margin-bottom: 4px; }
  .contact svg { width: 14px; height: 14px; flex: none; }
</style>
</head>
<body>

  <section class="card card-front" aria-label="Business card front">
    <div class="front-wordmark">
      <span class="dot" aria-hidden="true"></span>
      <span>KESTRA</span>
    </div>
  </section>

  <section class="card card-back" aria-label="Business card back">
    <div class="back-watermark" aria-hidden="true">KESTRA</div>

    <div class="back-logo">
      <div class="name">KESTRA</div>
      <div class="tagline">Integrated<br>Communications</div>
    </div>

    <div class="band-white"></div>
    <div class="band-orange"></div>
    <div class="band-logo">KESTRA</div>

    <div class="person">Marisolde (Olde) Fuentes</div>

    <ul class="contact">
      <li>
        <svg viewBox="0 0 16 16" aria-hidden="true"><path fill="#ffffff" d="M3.6 1.5l2.3 2.6-1.2 1.7c.9 1.9 2.4 3.4 4.3 4.3l1.7-1.2 2.6 2.3-1.3 2.3C7 13 3 9 1.3 3.1z"/></svg>
        <span>787-555-0148</span>
      </li>
      <li>
        <svg viewBox="0 0 16 16" aria-hidden="true"><rect x="1.5" y="3.5" width="13" height="9" fill="none" stroke="#ffffff" stroke-width="1.4"/><path d="M1.5 3.5l6.5 5 6.5-5" fill="none" stroke="#ffffff" stroke-width="1.4"/></svg>
        <span>ofuentes@kestrakom.example</span>
      </li>
    </ul>
  </section>

</body>
</html>
```